Trucking company specializing in intermodal containers

We need a logo design for our trucking company based in Kent, Washington. Our companies name is Varnell Haulways LLC, we specialize in intermodal containers, and work off of the Crestmark Rail Lines and the ports. We provide service by transporting freight with our fleet of trucks. We operate within Washington, Oregon, and Idaho. Our fleet consists of an east division and a local division. Our team motto currently is globally connected, locally invested.

Target Market(s)

brokers, intermodal management companies, customers

Industry/Entity Type

Trucking Company

Contact Information for Business Card

physical address 4153 N. 318th Pl Kent, WA 98417
office number is 253-555-0148

Font styles to use
Sans Serif

Colors

Designer to choose colors to be used in the design.

Requirements
Must have
• We need to update our current logo. Something like an emblem; that makes a statement that this logo/ sign represents Varnell Haulways. Something like a royal stamp but in this case a royal shield.
Nice to have
• simple, yet bold. something someone does not currently have. We need something fresh and exciting. Something that will also make a statement because currently our reputation is great within the industry and our community. But we need to reflect that we are professional and willing to provide the best service. We are open to new statement lines.
Should not have
• Should not have something thats been used before. We are open to suggestions that you have and a design that is completely unique and you make originally without what we want but what you like as well. Ofcourse it should still represent the industry we are in.

```html
<!DOCTYPE html>
<html lang="en">
<head>
<meta charset="utf-8">
<title>Varnell Haulways – Business Card</title>
<link rel="stylesheet" href="https://fonts.googleapis.com/css2?family=Didact+Gothic&display=swap">
<style>
  :root {
    --stage: #4a3a30;
    --teal: #2a7090;
    --white: #ffffff;
    --rule: #c9c9cb;
    --mark-grey: #bdbec0;
    --footer-dark: #3b3b3d;
    --footer-text: #e6e6e6;
  }
  * { margin: 0; padding: 0; box-sizing: border-box; }
  html, body {
    width: 1200px;
    height: 960px;
    overflow: hidden;
    background: var(--stage);
    font-family: "Didact Gothic", "Century Gothic", sans-serif;
  }
  .canvas { position: relative; width: 1200px; height: 960px; }

  .card {
    position: absolute;
    border-radius: 22px;
    overflow: hidden;
  }

  /* Stacked wordmark occupying the emblem area */
  .wordmark {
    position: absolute; left: 0; right: 0;
    display: flex; flex-direction: column; align-items: center;
    text-align: center;
    letter-spacing: 4px;
    line-height: 1.1;
  }
  .wordmark__square {
    background: currentColor;
    margin-bottom: 18px;
  }

  /* Front */
  .card--front {
    left: 245px; top: 32px; width: 752px; height: 438px;
    background: var(--white);
  }
  .card--front .wordmark {
    top: 78px;
    color: var(--teal);
    font-size: 46px;
  }
  .card--front .wordmark__square { width: 56px; height: 56px; }

  .card--front .rule {
    position: absolute; left: 0; right: 0; top: 330px; height: 5px;
    background: var(--rule);
  }
  .card--front .contact-band {
    position: absolute; left: 0; right: 0; top: 335px; bottom: 0;
    background: var(--teal);
    color: var(--white);
    text-align: center;
    font-size: 19px;
    padding-top: 14px;
    line-height: 34px;
  }
  .contact-band .sep { margin: 0 9px; }

  /* Back */
  .card--back {
    left: 243px; top: 478px; width: 756px; height: 427px;
    background: var(--teal);
  }
  .card--back .wordmark {
    top: 98px;
    color: var(--mark-grey);
    font-size: 52px;
  }
  .card--back .wordmark__square { width: 64px; height: 64px; }

  .card--back .rule {
    position: absolute; left: 0; right: 0; top: 380px; height: 5px;
    background: var(--rule);
  }
  .card--back .web-band {
    position: absolute; left: 0; right: 0; top: 385px; bottom: 0;
    background: var(--footer-dark);
    color: var(--footer-text);
    text-align: center;
    font-size: 14px;
    letter-spacing: 5px;
    line-height: 46px;
  }
</style>
</head>
<body>
<div class="canvas">
  <section class="card card--front">
    <div class="wordmark">
      <span class="wordmark__square"></span>
      <span class="wordmark__line">VARNELL</span>
      <span class="wordmark__line">HAULWAYS</span>
    </div>
    <div class="rule"></div>
    <div class="contact-band">
      <p class="address">4153 N. 318th Pl Kent, WA 98417</p>
      <p class="lines">253-555-0148<span class="sep">|</span>info@VarnellHaulways.com</p>
    </div>
  </section>

  <section class="card card--back">
    <div class="wordmark">
      <span class="wordmark__square"></span>
      <span class="wordmark__line">VARNELL</span>
      <span class="wordmark__line">HAULWAYS</span>
    </div>
    <div class="rule"></div>
    <div class="web-band">www.VARNELLHAULWAYS.com</div>
  </section>
</div>
</body>
</html>
```